Land Buying Company Needs Letterhead for Direct Mail Marketing to Land Owners

We are looking for a professional letterhead that we will be including in our direct mail marketing. We will be sending this to land owners who may be interested in selling or purchasing land.

The letterhead needs to be editable. Headers and footers would look nice, but we are open. We would want it to include our address, website, phone, and email info. For right now the address to use for design purposes would the following:

Address: 415 Bramwell Avenue #600
Dallas, TX 75219
Website - www.quillridgeacres.example
Email - info@quillridgeacres.example
Phone - 866-402-ACRE

I have attached our logo zip file that we just had done on Pixel Guild. Let me know what questions you have, and thank you.

```html
<!DOCTYPE html>
<html lang="en">
<head>
<meta charset="utf-8">
<title>Quillridge Acres Letterhead</title>
<link rel="stylesheet" href="https://fonts.googleapis.com/css2?family=Montserrat:wght@600&family=Lato:wght@400&display=swap">
<style>
  :root {
    --backdrop: #d6d6d6;
    --paper: #ffffff;
    --leaf: #98c93c;
    --forest: #475e2d;
  }
  html, body {
    margin: 0;
    padding: 0;
    width: 1056px;
    height: 1200px;
    overflow: hidden;
    background: var(--backdrop);
  }
  .letterhead {
    position: absolute;
    left: 118px;
    top: 20px;
    width: 820px;
    height: 1160px;
    background: var(--paper);
    overflow: hidden;
  }
  .side-band {
    position: absolute;
    left: 0;
    top: 0;
    width: 60px;
    height: 1160px;
  }
  .brand {
    position: absolute;
    left: 242px;
    top: 64px;
    display: flex;
    align-items: center;
    gap: 16px;
  }
  .brand-dot {
    width: 70px;
    height: 70px;
    border-radius: 50%;
    background: var(--forest);
  }
  .brand-name {
    font-family: "Montserrat", sans-serif;
    font-weight: 600;
    font-size: 34px;
    letter-spacing: 2px;
    color: var(--forest);
    text-transform: uppercase;
  }
  .contact {
    position: absolute;
    left: 62px;
    top: 991px;
    font-family: "Lato", sans-serif;
    font-size: 15.5px;
    line-height: 20px;
    color: var(--forest);
  }
  .contact p { margin: 0; }
  .contact .address { margin-bottom: 20px; }
  .contact .line { height: 23px; line-height: 23px; }
</style>
</head>
<body>
  <main class="letterhead">
    <svg class="side-band" viewBox="0 0 60 1160" width="60" height="1160" aria-hidden="true">
      <polygon points="0,0 40,0 40,309 0,286" fill="var(--leaf)"/>
      <polygon points="0,295 40,318 40,1160 0,1160" fill="var(--forest)"/>
      <rect x="22" y="982" width="31" height="146" fill="var(--forest)" stroke="#ffffff" stroke-width="3"/>
      <g fill="#ffffff">
        <!-- location pin -->
        <path d="M37 1004c-4.4 0-7.5 3.3-7.5 7.3 0 5 7.5 12 7.5 12s7.5-7 7.5-12c0-4-3.1-7.3-7.5-7.3zm0 10.2a3 3 0 1 1 0-6 3 3 0 0 1 0 6z"/>
        <!-- phone -->
        <path d="M31 1057c1-1 2.5-1 3 0l1.6 2.4c.5.8.2 1.6-.5 2.1l-1 .7c.8 2 2.3 3.6 4.2 4.5l.8-1c.6-.7 1.4-.8 2.1-.3l2.3 1.7c.8.6.8 1.8 0 2.6l-1.3 1.2c-4.5 1.1-12.3-6.7-11.8-11.6z"/>
        <path d="M38 1055a7 7 0 0 1 6.5 6.5" fill="none" stroke="#ffffff" stroke-width="1.4"/>
        <!-- envelope -->
        <rect x="30" y="1080" width="14" height="10" fill="none" stroke="#ffffff" stroke-width="1.4"/>
        <path d="M30 1080l7 6 7-6" fill="none" stroke="#ffffff" stroke-width="1.4"/>
        <!-- globe -->
        <g fill="none" stroke="#ffffff" stroke-width="1.3">
          <circle cx="37" cy="1109" r="6.5"/>
          <ellipse cx="37" cy="1109" rx="3" ry="6.5"/>
          <line x1="30.5" y1="1109" x2="43.5" y2="1109"/>
          <line x1="32" y1="1105.5" x2="42" y2="1105.5"/>
          <line x1="32" y1="1112.5" x2="42" y2="1112.5"/>
        </g>
      </g>
    </svg>

    <header class="brand">
      <div class="brand-dot"></div>
      <div class="brand-name">Quillridge Acres</div>
    </header>

    <footer class="contact">
      <div class="address">
        <p>415 Bramwell Avenue #600</p>
        <p>Dallas, TX 75219</p>
      </div>
      <p class="line">866-402-ACRE</p>
      <p class="line">info@quillridgeacres.example</p>
      <p class="line">www.quillridgeacres.example</p>
    </footer>
  </main>
</body>
</html>
```